Communication and Marketing agency needs a new presentation card

We are a group of communication and marketing agencies specialized in companies that are in the logistics and industrial sector. The head agency is TELVANO Grupo and the group consists of 4 agencies: TELVANO Media, TELVANO Digital, TELVANO Research and EnlazaPorImagen. We hace 4 offices in Spain (Madrid, Barcelona, Valencia and Murcia). We are looking for a clean and attractive design that transmits our experience, brand presence in the market and knowledge to those who receive the card.It has to maintain the colors of the logo that is attached.
Target Market(s)
logistics and industrial sector
Marketing department
Clean and attractive design

```html
<!DOCTYPE html>
<html lang="es">
<head>
<meta charset="utf-8">
<title>TELVANO Grupo – Business Card</title>
<link rel="stylesheet" href="https://fonts.googleapis.com/css2?family=Oswald:wght@400;500;600&family=Open+Sans:wght@400;700&display=swap">
<style>
  :root {
    --backdrop: #7b7c82;
    --card-light: #efefef;
    --card-dark: #48433f;
    --brand-red: #b01e24;
    --ink: #4a4643;
    --ink-soft: #d8d8d8;
  }
  * { box-sizing: border-box; margin: 0; padding: 0; }
  html, body { width: 1200px; height: 1144px; overflow: hidden; }
  body { background: var(--backdrop); position: relative; font-family: "Open Sans", sans-serif; }

  .card { position: absolute; left: 255px; width: 690px; height: 394px; }
  .card--front { top: 150px; background: linear-gradient(135deg, #f4f4f4, #e6e6e6); }
  .card--back { top: 603px; height: 393px; background: linear-gradient(135deg, #4c4744, #423d3a); }

  .brand { position: absolute; font-family: "Oswald", sans-serif; font-weight: 500; color: var(--brand-red); text-align: right; line-height: 1; }
  .brand__name { display: block; letter-spacing: 6px; }
  .brand__sub { display: block; }

  .card--front .brand { left: 185px; width: 322px; top: 40px; }
  .card--front .brand__name { font-size: 62px; }
  .card--front .brand__sub { font-size: 38px; margin-top: 6px; }

  .card--back .brand { left: 169px; width: 356px; top: 132px; }
  .card--back .brand__name { font-size: 68px; }
  .card--back .brand__sub { font-size: 42px; margin-top: 6px; }

  .person { position: absolute; left: 149px; top: 240px; width: 188px; text-align: right; font-family: "Oswald", sans-serif; }
  .person__name { font-size: 27px; font-weight: 600; color: var(--brand-red); letter-spacing: 0.5px; line-height: 1.1; }
  .person__role { font-size: 19px; font-weight: 400; color: var(--ink); line-height: 1.2; }

  .divider { position: absolute; left: 349px; top: 237px; width: 1.5px; height: 56px; background: var(--brand-red); }

  .contacts { position: absolute; left: 364px; top: 232px; list-style: none; }
  .contacts li { display: flex; align-items: center; height: 21px; font-size: 16px; color: var(--ink); }
  .contacts svg { width: 13px; height: 13px; margin-right: 7px; fill: var(--brand-red); flex: none; }

  .address { position: absolute; left: 149px; top: 332px; font-size: 16px; color: var(--ink); }
  .address strong { color: var(--brand-red); }

  .agencies { position: absolute; top: 300px; left: 0; width: 690px; display: flex; justify-content: center; gap: 22px; }
  .agency { font-family: "Oswald", sans-serif; font-weight: 400; font-size: 15px; letter-spacing: 1px; }
  .agency--light { color: var(--ink-soft); }
  .agency--red { color: var(--brand-red); }
</style>
</head>
<body>
  <section class="card card--front">
    <div class="brand"><span class="brand__name">TELVANO</span><span class="brand__sub">Grupo</span></div>

    <div class="person">
      <p class="person__name">ADRIÁN OLMEDO</p>
      <p class="person__role">Founder</p>
    </div>
    <div class="divider"></div>
    <ul class="contacts">
      <li><svg viewBox="0 0 16 16"><path d="M3.5 1l2.5 3-1.5 1.8c.9 2 2.6 3.7 4.7 4.7L11 9l3 2.5-1.3 2.8C7 14 2 9 1.7 3.3z"/></svg>(000) 987-210-44</li>
      <li><svg viewBox="0 0 16 16"><path d="M1 3h14v1.5L8 9 1 4.5z M1 6.3l7 4.5 7-4.5V13H1z"/></svg>hola@telvanogrupo.com</li>
      <li><svg viewBox="0 0 16 16"><circle cx="8" cy="8" r="7"/></svg>www.telvanogrupo.com</li>
    </ul>
    <p class="address"><strong>Address:</strong> 112 Calle del Prado, 28014 Madrid, Spain</p>
  </section>

  <section class="card card--back">
    <div class="brand"><span class="brand__name">TELVANO</span><span class="brand__sub">Grupo</span></div>
    <div class="agencies">
      <span class="agency agency--light">TELVANO Research</span>
      <span class="agency agency--red">TELVANO Media</span>
      <span class="agency agency--light">TELVANO Digital</span>
    </div>
  </section>
</body>
</html>
```